Cleaning Company Banner

Looking to have a Banner made that shows our contact information and shows what we do with good imagery to catch cars driving by. Will be a 6' x 3' banner (landscape). Attached our logo and flyer that we currently hand out.

```html
<!DOCTYPE html>
<html lang="en">
<head>
<meta charset="utf-8">
<title>BrightMark Cleaning Banner</title>
<link href="https://fonts.googleapis.com/css2?family=Bebas+Neue&family=Montserrat:wght@500;600;700&display=swap" rel="stylesheet">
<style>
  :root{
    --page:#f2f2f2;
    --teal:#1bb8a8;
    --navy:#0a6a9c;
    --ink:#2b2b2b;
    --white:#ffffff;
    --mist:#e6f3fa;
  }
  *{margin:0;padding:0;box-sizing:border-box}
  html,body{width:1200px;height:1200px;overflow:hidden;background:var(--page)}
  body{position:relative;font-family:"Montserrat",sans-serif}
  .banner{position:absolute;left:40px;top:355px;width:1120px;height:490px;overflow:hidden;
    background:linear-gradient(90deg,var(--white) 0%,var(--white) 30%,var(--mist) 55%);
    box-shadow:0 6px 14px rgba(0,0,0,.18)}
  .photo{position:absolute;left:420px;top:0;width:400px;height:490px;
    background:
      radial-gradient(ellipse 90px 140px at 300px 110px,rgba(240,210,40,.95),rgba(240,210,40,0) 70%),
      radial-gradient(ellipse 200px 170px at 250px 380px,#1f86d6,rgba(31,134,214,0) 80%),
      radial-gradient(ellipse 160px 140px at 180px 120px,#8cc6e6,rgba(140,198,230,0) 80%),
      linear-gradient(90deg,rgba(255,255,255,0) 0%,#cfe7f3 35%,#9fcbe2 100%)}
  .curve{position:absolute;left:0;top:0;width:1120px;height:490px}
  .brand{position:absolute;left:110px;top:40px;width:290px;text-align:center;color:var(--teal)}
  .brand-dot{display:block;width:70px;height:70px;border-radius:50%;background:var(--teal);margin:0 auto 14px}
  .brand-name{font-weight:600;font-size:34px;letter-spacing:2px;line-height:1}
  .brand-sub{font-weight:600;font-size:34px;letter-spacing:2px;line-height:1.05}
  .tagline{position:absolute;left:30px;top:230px;width:430px;text-align:center;
    font-family:"Bebas Neue",sans-serif;font-size:31px;line-height:1.02;color:var(--ink);letter-spacing:.3px}
  .name-band{position:absolute;left:0;top:336px;width:320px;height:34px;background:var(--teal);
    border-radius:0 17px 17px 0;color:var(--white);font-weight:700;font-size:23px;letter-spacing:.5px;
    padding-left:42px;line-height:34px}
  .role{position:absolute;left:39px;top:372px;font-size:20px;font-weight:500;color:var(--ink)}
  .phone-icon{position:absolute;left:38px;top:409px;width:35px;height:35px}
  .call-label{position:absolute;left:87px;top:400px;font-size:16px;font-weight:600;color:var(--teal)}
  .phone{position:absolute;left:83px;top:417px;font-size:24px;font-weight:700;color:var(--ink)}
  .email{position:absolute;left:39px;top:451px;font-size:19px;font-weight:500;color:var(--ink)}
  .services-pill{position:absolute;left:824px;top:90px;width:296px;height:34px;background:var(--teal);
    border-radius:17px 0 0 17px;color:var(--white);font-weight:700;font-size:24px;text-align:center;
    line-height:34px;letter-spacing:.5px}
  .service-list{position:absolute;left:852px;top:168px;list-style:none}
  .service{display:flex;align-items:center;height:71px}
  .service-icon{width:42px;height:42px;margin-right:27px;flex:none}
  .service-text{color:var(--white);font-weight:600;font-size:24px;line-height:1}
</style>
</head>
<body>
  <main class="banner">
    <div class="photo" role="img" aria-label="Photo of a yellow-gloved hand holding a blue bucket of cleaning supplies"></div>

    <svg class="curve" viewBox="0 0 1120 490" aria-hidden="true">
      <path d="M700 0 C690 150 830 320 788 490 L1120 490 L1120 0 Z" fill="var(--teal)"/>
      <path d="M752 0 C742 150 872 320 830 490 L1120 490 L1120 0 Z" fill="var(--navy)"/>
    </svg>

    <div class="brand">
      <span class="brand-dot"></span>
      <div class="brand-name">BRIGHTMARK</div>
      <div class="brand-sub">CLEANING</div>
    </div>

    <p class="tagline">Quality driven and reliable to take<br>care of all your cleaning needs!!!</p>

    <div class="name-band">DANA WHITFIELD</div>
    <div class="role">Owner | Operator</div>
    <svg class="phone-icon" viewBox="0 0 36 36" aria-hidden="true">
      <circle cx="18" cy="18" r="18" fill="var(--teal)"/>
      <path d="M12 9 l4 0 l2 6 l-3 2 c1.5 3 3.5 5 6 6 l2-3 l6 2 l0 4 c0 1-1 2-2 2 c-9 0-17-8-17-17 c0-1 1-2 2-2z" fill="var(--white)"/>
    </svg>
    <div class="call-label">Call or Text:</div>
    <div class="phone">(555) 014-2270</div>
    <div class="email">hello@brightmarkclean.com</div>

    <div class="services-pill">SERVICES:</div>
    <ul class="service-list">
      <li class="service">
        <svg class="service-icon" viewBox="0 0 42 42" aria-hidden="true"><rect x="4" y="4" width="34" height="34" rx="6" fill="none" stroke="var(--white)" stroke-width="3"/><path d="M12 21 l6 6 l12-13" fill="none" stroke="var(--white)" stroke-width="3.5"/></svg>
        <span class="service-text">Residential<br>Cleaning</span>
      </li>
      <li class="service">
        <svg class="service-icon" viewBox="0 0 42 42" aria-hidden="true"><rect x="4" y="4" width="34" height="34" rx="6" fill="none" stroke="var(--white)" stroke-width="3"/><path d="M12 21 l6 6 l12-13" fill="none" stroke="var(--white)" stroke-width="3.5"/></svg>
        <span class="service-text">Commercial<br>Cleaning</span>
      </li>
      <li class="service">
        <svg class="service-icon" viewBox="0 0 42 42" aria-hidden="true"><rect x="4" y="4" width="34" height="34" rx="6" fill="none" stroke="var(--white)" stroke-width="3"/><path d="M12 21 l6 6 l12-13" fill="none" stroke="var(--white)" stroke-width="3.5"/></svg>
        <span class="service-text">Antiviral<br>Disinfection</span>
      </li>
      <li class="service">
        <svg class="service-icon" viewBox="0 0 42 42" aria-hidden="true"><rect x="4" y="4" width="34" height="34" rx="6" fill="none" stroke="var(--white)" stroke-width="3"/><path d="M12 21 l6 6 l12-13" fill="none" stroke="var(--white)" stroke-width="3.5"/></svg>
        <span class="service-text">Construction<br>Cleaning</span>
      </li>
    </ul>
  </main>
</body>
</html>
```